Crestwell Renewal Business Card Design Phase 2

Professional and clean design. The design colors should flow with the logo. Two-sided card with the website on the back which is:

www.CrestwellRenewal.example.

"Specializing in Water Damage Restoration"

On the front I need the name, email, phone, and logo.

Name: Dorian Halvek
Email: Dorian@CrestwellRenewal.example
Phone: 555-318-2046 for now

I only have the Preview and Thumbnail right now but should have the source files uploaded within a day or two.

Target Market(s)

Flood victims, home owners with water damage from busted pipes etc...

Industry/Entity Type

Business

Contact Information for Business Card

Name: Dorian Halvek

Font styles to use
Serif
Sans Serif

Requirements
Must have
• Business Card Details Info

```html
<!DOCTYPE html>
<html lang="en">
<head>
<meta charset="utf-8">
<title>Crestwell Renewal – Business Card</title>
<link rel="stylesheet" href="https://fonts.googleapis.com/css2?family=Tinos:wght@400;700&display=swap">
<style>
  :root {
    --navy: #1c3363;
    --green: #4a8e3f;
    --paper: #ffffff;
    --backdrop: #e9eaec;
    --shadow: rgba(20, 24, 32, 0.18);
  }
  * { margin: 0; padding: 0; box-sizing: border-box; }
  html, body {
    width: 1200px; height: 780px; overflow: hidden;
    background: var(--backdrop);
    font-family: "Tinos", "Times New Roman", serif;
  }
  .sheet {
    width: 1200px; height: 780px;
    display: flex; align-items: center; justify-content: center; gap: 60px;
  }
  .card {
    position: relative;
    width: 540px; height: 309px;
    background: var(--paper);
    box-shadow: 0 10px 28px var(--shadow);
    overflow: hidden;
  }
  .brand__name {
    color: var(--navy); font-weight: 700;
    letter-spacing: 1px; text-transform: uppercase; line-height: 1;
  }
  .brand__line { display: block; white-space: nowrap; }

  /* Back side */
  .card--back .brand {
    position: absolute; left: 0; right: 0; top: 78px;
    display: flex; align-items: center; justify-content: center; gap: 16px;
  }
  .brand__dot {
    flex: 0 0 auto;
    width: 20px; height: 20px; border-radius: 50%; background: var(--green);
  }
  .card--back .brand__name { font-size: 48px; text-align: left; }
  .card--back .website {
    position: absolute; left: 0; right: 0; top: 204px;
    text-align: center; color: var(--navy); font-size: 15px;
  }

  /* Front side */
  .card__swoosh { position: absolute; inset: 0; }
  .front-info {
    position: absolute; right: 26px; top: 30px; width: 300px;
    text-align: right;
  }
  .front-info .brand__name { font-size: 30px; }
  .tagline {
    margin-top: 8px; color: var(--navy); font-size: 12.5px;
  }
  .person {
    margin-top: 12px; color: var(--navy); font-size: 19px;
    letter-spacing: 0.5px; text-transform: uppercase;
  }
  .contact { margin-top: 16px; list-style: none; }
  .contact__item {
    display: flex; justify-content: flex-end; align-items: center; gap: 8px;
    color: var(--green); font-size: 14.5px; line-height: 22px; white-space: nowrap;
  }
  .contact__icon {
    width: 15px; height: 15px; border-radius: 50%; background: var(--navy);
    display: inline-flex; align-items: center; justify-content: center;
  }
  .contact__icon svg { width: 9px; height: 9px; }
</style>
</head>
<body>
<main class="sheet">

  <section class="card card--back" aria-label="Card back">
    <div class="brand">
      <span class="brand__dot"></span>
      <span class="brand__name"><span class="brand__line">Crestwell</span><span class="brand__line">Renewal</span></span>
    </div>
    <p class="website">www.CrestwellRenewal.example.</p>
  </section>

  <section class="card card--front" aria-label="Card front">
    <svg class="card__swoosh" viewBox="0 0 540 309" width="540" height="309" aria-hidden="true">
      <path d="M0,0 L92,0 C108,170 225,288 372,309 L0,309 Z" fill="var(--green)"/>
      <path d="M106,0 C121,162 236,276 392,309" fill="none" stroke="var(--navy)" stroke-width="9"/>
    </svg>

    <div class="front-info">
      <div class="brand__name"><span class="brand__line">Crestwell</span><span class="brand__line">Renewal</span></div>
      <p class="tagline">Specializing in Water Damage Restoration</p>
      <p class="person">Dorian Halvek</p>
      <ul class="contact">
        <li class="contact__item">555-318-2046
          <span class="contact__icon"><svg viewBox="0 0 10 10"><path d="M2 1 L4 1 L4.6 3 L3.5 3.8 C4 5 5 6 6.2 6.5 L7 5.4 L9 6 L9 8 C5 8.5 1.5 5 2 1 Z" fill="#fff"/></svg></span>
        </li>
        <li class="contact__item">Dorian@CrestwellRenewal.example
          <span class="contact__icon"><svg viewBox="0 0 10 10"><rect x="1" y="2.5" width="8" height="5" fill="none" stroke="#fff" stroke-width="1"/><path d="M1 2.5 L5 5.5 L9 2.5" fill="none" stroke="#fff" stroke-width="1"/></svg></span>
        </li>
        <li class="contact__item">www.CrestwellRenewal.example.
          <span class="contact__icon"><svg viewBox="0 0 10 10"><circle cx="5" cy="5" r="3.8" fill="none" stroke="#fff" stroke-width="1"/><ellipse cx="5" cy="5" rx="1.6" ry="3.8" fill="none" stroke="#fff" stroke-width="0.8"/><path d="M1.2 5 H8.8" stroke="#fff" stroke-width="0.8"/></svg></span>
        </li>
      </ul>
    </div>
  </section>

</main>
</body>
</html>
```